New Organic Skin Care Line Needs to Design a Product Label

***THE WINNER OF THIS PROJECT WILL MOST LIKELY BECOME THE EXCLUSIVE DESIGNER FOR OUR OTHER PRODUCT LABELS***

We need a label design for a new organic skin care product line called "Maple Fern Gala." This specific product is a 100% pure organic coconut oil. It's used for skin hydration, protection, and makeup removal.

Info to include on front label:

1. Logo: Maple Fern Gala (attached)
2. Product Name: Pure Coconut Oil (emphasize "organic" somewhere)
3. Slogan: Hydrate your skin and hair.
4. Size: 8 FL OZ 236mL

Attached is:

1. The brand logo "Maple Fern Gala" with a white background.
2. An image of the bottle we will use.
3. An image of the bottle with lines to show the size and placement of the label.
4. The brand logo "Maple Fern Gala" with a black background. (photoshop file)

What we need:

A simple mock up of the front side of the label on the bottle. We first want to know what it will look like on the bottle given the size and dimensions.

- We would like one label with a white background (including the logo with a white background).
- We would like a second label with a black background (including the logo with a black background, just need to make the black font white instead of black).

We can get a great idea of what to expect from the front side of the label so we will complete the back side once we identify a winner.
Updates

Apologies, but we are now using a different bottle. The previous one is now discontinued. Please view the two most recent images uploaded. One is an image of the new bottle by itself. The other is an image of that bottle with instructions. Please use your most recent designs on the new bottle. Feel free to make any modifications you see fit to compliment the new bottle shape. Added Friday, March 18, 2016

Reason: We are still working with the label company to finalize the size. Once the size is confirmed we will have to tweak labels based on finalized measurements.

Target Market(s)

Women, 18-70

Industry/Entity Type

Skin Care Product

Font styles to use
Decorative
Script

Requirements
Must have
• -"shabby sheek" and "cute" theme
• -soft organic feel
• -the ingredients are organic, pure, and natural. That should be an essence of the label.

```html
<!DOCTYPE html>
<html lang="en">
<head>
<meta charset="utf-8">
<title>Maple Fern Gala – Pure Coconut Oil Label Mockup</title>
<link rel="stylesheet" href="https://fonts.googleapis.com/css2?family=Cormorant+Garamond:wght@500;600&family=Kalam:wght@700&family=Open+Sans:wght@700&display=swap">
<style>
  :root {
    --paper: #ffffff;
    --ink: #000000;
    --label-black: #141414;
    --label-white: #ffffff;
    --accent-pink: #e0297f;
    --glass-light: #f3f4f5;
    --glass-mid: #dcdee0;
    --glass-dark: #b5b8bb;
    --grey-text: #8a8a8a;
    --tagline: #a7a7a9;
    --tagline-shadow: #4a4a4a;
  }
  * { margin: 0; padding: 0; box-sizing: border-box; }
  html, body {
    width: 1200px; height: 868px; overflow: hidden;
    background: var(--paper);
  }
  .canvas { position: relative; width: 1200px; height: 868px; }
  .artboard { position: absolute; inset: 0; }
  .size-note {
    position: absolute; left: 0; width: 1226px; top: 552px;
    text-align: center;
    font-family: "Open Sans", Arial, sans-serif;
    font-weight: 700; font-size: 16px;
    color: var(--grey-text);
  }
  .tagline {
    position: absolute; left: 0; width: 1234px; top: 698px;
    text-align: center;
    font-family: "Kalam", "Comic Sans MS", cursive;
    font-weight: 700; font-size: 48px; line-height: 50px;
    color: var(--tagline);
    text-shadow: 2px 2px 0 var(--tagline-shadow);
  }
</style>
</head>
<body>
<div class="canvas">
  <svg class="artboard" width="1200" height="868" viewBox="0 0 1200 868" xmlns="http://www.w3.org/2000/svg" xmlns:xlink="http://www.w3.org/1999/xlink">
    <defs>
      <linearGradient id="glass" x1="0" y1="0" x2="1" y2="0">
        <stop offset="0" stop-color="var(--glass-dark)"/>
        <stop offset="0.35" stop-color="var(--glass-light)"/>
        <stop offset="0.7" stop-color="var(--glass-mid)"/>
        <stop offset="1" stop-color="var(--glass-dark)"/>
      </linearGradient>

      <!-- Label copy, laid out around the label centre (0,0) -->
      <g id="label-copy" fill="currentColor" text-anchor="middle">
        <circle class="brand-dot" cx="0" cy="-48" r="10" fill="none" stroke="var(--accent-pink)" stroke-width="2"/>
        <text class="product-name" x="0" y="-8" font-family="'Cormorant Garamond', Georgia, serif" font-weight="600" font-size="17">Pure Coconut Oil</text>
        <text class="product-claim" x="0" y="11" font-family="'Cormorant Garamond', Georgia, serif" font-weight="600" font-size="10" letter-spacing="3" fill="var(--accent-pink)">ORGANIC</text>
        <text class="brand-name" x="0" y="50" font-family="'Cormorant Garamond', Georgia, serif" font-weight="500" font-size="16" letter-spacing="2.5">MAPLE FERN GALA</text>
        <text class="product-size" x="0" y="70" font-family="'Cormorant Garamond', Georgia, serif" font-weight="600" font-size="10" letter-spacing="1.5">8 FL OZ 236mL</text>
      </g>
    </defs>

    <!-- Left bottle with white label and placement guides -->
    <g class="bottle bottle--white">
      <path class="bottle-photo" role="img" aria-label="Photo of the clear glass teardrop bottle"
            d="M300 156 H376 V196 C376 300 390 380 420 458 C456 540 456 644 420 676 C398 692 278 692 256 676 C220 644 220 540 256 458 C286 380 300 300 300 196 Z"
            fill="url(#glass)" opacity="0.6"/>
      <circle class="label label--white" cx="338" cy="586" r="104" fill="var(--label-white)" stroke="var(--ink)" stroke-width="3"/>
      <line class="guide" x1="222" y1="482" x2="454" y2="482" stroke="var(--ink)" stroke-width="6"/>
      <line class="guide" x1="222" y1="692" x2="459" y2="692" stroke="var(--ink)" stroke-width="6"/>
      <use href="#label-copy" xlink:href="#label-copy" transform="translate(338 586) scale(0.9)" style="color: var(--ink)"/>
    </g>

    <!-- Flat white label -->
    <g class="label-flat label-flat--white">
      <path d="M547 104 H657 A114 114 0 1 1 547 104 Z" fill="var(--label-white)" stroke="var(--ink)" stroke-width="3"/>
      <use href="#label-copy" xlink:href="#label-copy" transform="translate(602 196)" style="color: var(--ink)"/>
    </g>

    <!-- Flat black label -->
    <g class="label-flat label-flat--black">
      <path d="M541 336 H679 A115 115 0 1 1 541 336 Z" fill="var(--label-black)"/>
      <use href="#label-copy" xlink:href="#label-copy" transform="translate(609 430)" style="color: var(--label-white)"/>
    </g>

    <!-- Right bottle with black label -->
    <g class="bottle bottle--black">
      <path class="bottle-photo" role="img" aria-label="Photo of the clear glass teardrop bottle"
            d="M850 156 H924 V196 C924 300 940 390 972 470 C1006 550 1006 650 970 680 C948 696 850 696 828 680 C790 650 790 550 824 470 C856 390 850 300 850 196 Z"
            fill="url(#glass)" opacity="0.6"/>
      <path class="label label--black" d="M846 476 H946 A110 110 0 1 1 846 476 Z" fill="var(--label-black)"/>
      <use href="#label-copy" xlink:href="#label-copy" transform="translate(896 582) scale(0.86)" style="color: var(--label-white)"/>
    </g>
  </svg>

  <p class="size-note">8 FL OZ 236mL</p>
  <p class="tagline">Pure Coconut Oil, Organic<br>Hydrate your skin and hair.</p>
</div>
</body>
</html>
```